Software Company Business Card Design

We are looking for a business card design for a software, messaging & IT services company based in Australia.

Lumora Group is the holding company for 3 brands all offering technology based business solutions; Lumora, Velbrix & Quillray. Brand Identity = Friendly, Professional, Viable, Vibrant, Creative

We want our business card to reflect that we are an innovative market leader. The design should be clean, professional and original.

This design will be used for all 3 brands.

More information about our company can be found at: www.lumoragroup-example.com.au
www.velbrix-example.com.au

Details we would like on the card:

Firstname Lastname
Position
Level 17, 248 Tarrow St
North Sydney
NSW 2060
Phone: +61 2 9387 2600
Fax: +61 2 9387 2611
Mobile:
Email:
www.lumoragroup-example.com.au

Target Market(s)

Our business cards are given to B2B and industry professionals.

Industry/Entity Type

Business

Requirements
Must have
• The Business Card must include the same colours as the logo.
Nice to have
• We would like it to me double sided.

```html
<!DOCTYPE html>
<html lang="en">
<head>
<meta charset="utf-8">
<title>Lumora Group – Business Card Set</title>
<link rel="stylesheet" href="https://fonts.googleapis.com/css2?family=Open+Sans:wght@400;600;700&display=swap">
<style>
  :root {
    --crimson: #b0103a;
    --crimson-deep: #8e0a1e;
    --maroon: #6e0712;
    --paper: #ffffff;
    --slate: #9295b6;
    --stage-light: #6a6a6a;
    --stage-dark: #050505;
  }
  html, body {
    margin: 0;
    padding: 0;
    width: 1200px;
    height: 815px;
    overflow: hidden;
  }
  .board {
    position: relative;
    width: 1200px;
    height: 815px;
    background: radial-gradient(ellipse at 50% 50%, var(--stage-light) 0%, #2a2a2a 55%, var(--stage-dark) 100%);
    font-family: "Open Sans", sans-serif;
  }
  .card {
    position: absolute;
    width: 371px;
    height: 249px;
    background: var(--paper);
    overflow: hidden;
  }
  .card .wave {
    position: absolute;
    left: 0;
    top: 0;
    width: 100%;
    height: 100%;
  }
  .card--group   { left: 38px;  top: 26px; }
  .card--family  { left: 784px; top: 26px; }
  .card--details { left: 411px; top: 275px; background: var(--crimson); }
  .card--quillray { left: 38px;  top: 523px; }
  .card--velbrix  { left: 784px; top: 523px; }

  .brand {
    position: absolute;
    margin: 0;
    font-weight: 700;
    white-space: nowrap;
    letter-spacing: -0.5px;
    line-height: 1;
  }
  .brand--hero {
    left: 0;
    width: 100%;
    text-align: center;
    top: 50px;
    font-size: 36px;
  }
  .brand--group { color: var(--crimson); }
  .brand--quillray { color: var(--crimson); }
  .brand--velbrix { color: var(--slate); }
  .brand--on-wave {
    color: var(--paper);
    font-size: 20px;
    bottom: 18px;
  }
  .card--family .brand--velbrix-tag { left: 22px; }
  .card--family .brand--quillray-tag { right: 22px; }
  .card--quillray .brand--on-wave,
  .card--velbrix .brand--on-wave { right: 16px; }

  .details {
    position: absolute;
    inset: 0;
    color: var(--paper);
  }
  .details .name {
    position: absolute;
    left: 21px;
    top: 11px;
    margin: 0;
    font-size: 18px;
    font-weight: 400;
  }
  .details .position {
    position: absolute;
    left: 21px;
    top: 35px;
    margin: 0;
    font-size: 13px;
  }
  .details .address,
  .details .contact {
    position: absolute;
    top: 84px;
    margin: 0;
    font-size: 11px;
    font-weight: 600;
    line-height: 15.5px;
    font-style: normal;
  }
  .details .address { left: 21px; }
  .details .contact { left: 185px; }
</style>
</head>
<body>
<main class="board">

  <section class="card card--group" aria-label="Lumora Group card front">
    <svg class="wave" viewBox="0 0 371 249" preserveAspectRatio="none" aria-hidden="true">
      <path d="M0,150 C110,198 220,206 371,140 L371,249 L0,249 Z" fill="var(--maroon)"/>
      <path d="M0,160 C110,208 220,214 371,152 L371,249 L0,249 Z" fill="var(--crimson-deep)"/>
      <path d="M0,172 C120,216 230,222 371,168 L371,249 L0,249 Z" fill="var(--crimson)"/>
    </svg>
    <p class="brand brand--hero brand--group">Lumora Group</p>
  </section>

  <section class="card card--family" aria-label="Lumora Group family card front">
    <svg class="wave" viewBox="0 0 371 249" preserveAspectRatio="none" aria-hidden="true">
      <path d="M0,150 C110,198 220,206 371,140 L371,249 L0,249 Z" fill="var(--maroon)"/>
      <path d="M0,160 C110,208 220,214 371,152 L371,249 L0,249 Z" fill="var(--crimson-deep)"/>
      <path d="M0,172 C120,216 230,222 371,168 L371,249 L0,249 Z" fill="var(--crimson)"/>
    </svg>
    <p class="brand brand--hero brand--group">Lumora Group</p>
    <p class="brand brand--on-wave brand--velbrix-tag">Velbrix</p>
    <p class="brand brand--on-wave brand--quillray-tag">Quillray</p>
  </section>

  <section class="card card--details" aria-label="Contact details side">
    <svg class="wave" viewBox="0 0 371 249" preserveAspectRatio="none" aria-hidden="true">
      <path d="M0,188 C110,232 230,176 371,158 L371,249 L0,249 Z" fill="var(--crimson-deep)" opacity="0.5"/>
      <path d="M0,196 C110,238 230,180 371,164 L371,249 L0,249 Z" fill="var(--paper)"/>
    </svg>
    <div class="details">
      <h1 class="name">Firstname Lastname</h1>
      <p class="position">Position</p>
      <address class="address">Level 17, 248 Tarrow St<br>North Sydney<br>NSW 2060</address>
      <p class="contact">Phone: +61 2 9387 2600<br>Fax: +61 2 9387 2611<br>Mobile:<br>Email:<br>www.lumoragroup-example.com.au</p>
    </div>
  </section>

  <section class="card card--quillray" aria-label="Quillray card front">
    <svg class="wave" viewBox="0 0 371 249" preserveAspectRatio="none" aria-hidden="true">
      <path d="M0,150 C110,198 220,206 371,140 L371,249 L0,249 Z" fill="var(--maroon)"/>
      <path d="M0,160 C110,208 220,214 371,152 L371,249 L0,249 Z" fill="var(--crimson-deep)"/>
      <path d="M0,172 C120,216 230,222 371,168 L371,249 L0,249 Z" fill="var(--crimson)"/>
    </svg>
    <p class="brand brand--hero brand--quillray">Quillray</p>
    <p class="brand brand--on-wave">Lumora Group</p>
  </section>

  <section class="card card--velbrix" aria-label="Velbrix card front">
    <svg class="wave" viewBox="0 0 371 249" preserveAspectRatio="none" aria-hidden="true">
      <path d="M0,150 C110,198 220,206 371,140 L371,249 L0,249 Z" fill="var(--maroon)"/>
      <path d="M0,160 C110,208 220,214 371,152 L371,249 L0,249 Z" fill="var(--crimson-deep)"/>
      <path d="M0,172 C120,216 230,222 371,168 L371,249 L0,249 Z" fill="var(--crimson)"/>
    </svg>
    <p class="brand brand--hero brand--velbrix">Velbrix</p>
    <p class="brand brand--on-wave">Lumora Group</p>
  </section>

</main>
</body>
</html>
```